" SOMOS UMA EMPRESA RECÉM CRIADA (FEVEREIRO DE 2015) E ESTAMOS ESTABELECIDOS NA CIDADE DE SAO JOSÉ DOS CAMPOS. TRATA-SE DE UM ESCRITORIO DE ADVOCACIA QUE É ESPECIALIZADO NA AREA DO DIREITO TRABALHISTA PATRONAL (ADVOGAMOS APENAS PARA EMPRESAS) E DIREITO ADMINISTRATIVO. "

```html
<!DOCTYPE html>
<html lang="pt-BR">
<head>
<meta charset="utf-8">
<title>Envelope – Barros Tavares &amp; Lima Neto</title>
<link href="https://fonts.googleapis.com/css2?family=Cinzel:wght@600&family=Open+Sans:wght@400;600&display=swap" rel="stylesheet">
<style>
  :root{
    --bg:#e4e5e7;
    --navy:#2f3a52;
    --navy-light:#3c4966;
    --accent:#2d9cd6;
    --text:#e8ecf3;
    --muted:#aab3c4;
    --flap:#ffffff;
  }
  *{box-sizing:border-box;margin:0;padding:0}
  html,body{width:1200px;height:1200px;overflow:hidden}
  body{background:var(--bg);font-family:"Open Sans",sans-serif;position:relative}
  .envelope{
    position:absolute;left:100px;width:1000px;height:470px;
    background:radial-gradient(ellipse at 45% 45%,var(--navy-light) 0%,var(--navy) 70%);
    box-shadow:0 6px 18px rgba(0,0,0,.18);
  }
  .envelope--back{top:80px}
  .envelope--front{top:650px}
  .flap-edge{position:absolute;top:0;right:0;width:120px;height:100%}
  .decoration{
    position:absolute;left:250px;top:20px;width:360px;height:360px;border-radius:50%;
    background:radial-gradient(circle,rgba(255,255,255,.07) 0%,rgba(255,255,255,0) 70%);
  }
  .brand{position:absolute;text-align:center;color:var(--text)}
  .brand__name{font-family:"Cinzel",serif;font-weight:600;font-size:17px;letter-spacing:1px;display:flex;align-items:center;justify-content:center;gap:10px}
  .brand__dot{width:14px;height:14px;border-radius:50%;background:var(--muted)}
  .brand__tagline{font-size:11px;color:var(--muted);letter-spacing:1.5px;margin-top:4px;text-transform:lowercase}
  .envelope--back .brand{right:150px;bottom:110px}
  .envelope--front .brand{left:0;right:0;top:120px}
  .contacts{
    position:absolute;left:30px;right:30px;bottom:28px;
    display:flex;justify-content:space-between;align-items:center;
  }
  .contact{display:flex;align-items:center;gap:10px;color:var(--text);font-size:12px;font-weight:600;line-height:1.45}
  .contact__icon{width:26px;height:26px;border-radius:50%;background:var(--accent);display:flex;align-items:center;justify-content:center;flex-shrink:0}
  .contact__icon svg{width:14px;height:14px}
</style>
</head>
<body>

<section class="envelope envelope--back">
  <svg class="flap-edge" viewBox="0 0 120 470" preserveAspectRatio="none" aria-hidden="true">
    <polygon points="0,0 120,0 120,470 100,470 100,20 0,20" fill="var(--flap)" opacity=".95"/>
  </svg>
  <div class="decoration" role="img" aria-label="Large faint brand symbol as background decoration"></div>
  <div class="brand">
    <div class="brand__name"><span class="brand__dot"></span>Barros Tavares &amp; Lima Neto</div>
    <div class="brand__tagline">Advocacia Empresarial</div>
  </div>
</section>

<section class="envelope envelope--front">
  <svg class="flap-edge" viewBox="0 0 120 470" preserveAspectRatio="none" aria-hidden="true">
    <polygon points="0,0 120,0 120,470 100,470 100,20 0,20" fill="var(--flap)" opacity=".95"/>
  </svg>
  <div class="brand">
    <div class="brand__name"><span class="brand__dot"></span>Barros Tavares &amp; Lima Neto</div>
    <div class="brand__tagline">Advocacia Empresarial</div>
  </div>
  <div class="contacts">
    <div class="contact">
      <span class="contact__icon"><svg viewBox="0 0 24 24"><path d="M12 2a7 7 0 0 0-7 7c0 5 7 13 7 13s7-8 7-13a7 7 0 0 0-7-7zm0 9.5A2.5 2.5 0 1 1 12 6.5a2.5 2.5 0 0 1 0 5z" fill="#fff"/></svg></span>
      <span>Rua das Palmeiras, 220 / 305 - Centro<br>São José dos Campos - SP - CEP: 12210-00</span>
    </div>
    <div class="contact">
      <span class="contact__icon"><svg viewBox="0 0 24 24"><path d="M6.6 10.8a15 15 0 0 0 6.6 6.6l2.2-2.2a1 1 0 0 1 1-.25 11.4 11.4 0 0 0 3.6.57 1 1 0 0 1 1 1V20a1 1 0 0 1-1 1A17 17 0 0 1 3 4a1 1 0 0 1 1-1h3.5a1 1 0 0 1 1 1c0 1.25.2 2.45.57 3.6a1 1 0 0 1-.25 1z" fill="#fff"/></svg></span>
      <span>(12) 3941 5520<br>(12) 3941 5521</span>
    </div>
    <div class="contact">
      <span class="contact__icon"><svg viewBox="0 0 24 24"><path d="M3 5h18v14H3z" fill="#fff"/><path d="M3 5l9 7 9-7" fill="none" stroke="var(--accent)" stroke-width="2"/></svg></span>
      <span>contato@btln.adv.br<br>www.btln.adv.br</span>
    </div>
  </div>
</section>

</body>
</html>
```